Junk Removal Website Design

We are working with a Junk Removal company in California. They provide junk hauling services for commercial and residential throughout California.
Some sites to use for inspiration:
https://www.1877binclear.com
https://haulwaycleanoutpro.com
https://www.quarrybrawnmovingclutter.com
https://www.clutterliftwardens.com
Thank you for taking the time to consider designing a website for us. We are web developers based in Stockton, CA, USA. Most of our projects go through the same process. Understanding this process may help you win a project with us. We custom-code all of our websites in-house. We don’t have any requirements as to what tools you use for your design, but we ask that you follow these guidelines.
IMAGES:
If you use any images or icons in the design, we ask that you have a link to the asset so we can purchase the image/icon. Most of the designs we submit do not have the customer’s images on them unless they have some great images. Be creative; show us the feeling you are trying to portray with your image choices. Use any royalty-free site you choose. We subscribe to Vexaro and mainly use their images, but we can purchase images outside of Vexaro. PLEASE NOTE: we will not submit designs to clients with watermarks on the images.
FONTS:
We ask that you identify the fonts you’re using in the design. This can be done in a message if you want. We typically use Plimbet Fonts and Vexaro Fonts.
CONTENT:
We're always open to different content and ideas. We often submit designs with stock images so the client can see our vision. We typically take pictures after the website launch to use their images with our vision. Lorem Ipsum is fine for paragraphs, but we ask that you make the Headers with correct English. We want to be able to show the vision and identify the sections of the website.
INSPIRATION:
We typically add a couple of links in the brief of websites we like to help you get started in your design.
REVISIONS:
We do not often ask for revisions of the designs unless we see something in the design that may not appeal to the client. If there are slight changes that we want to make, we do that in the development process.
FEEDBACK:
We rarely give feedback on designs during the design process. We are working on many website projects and do not have the time to provide feedback. We usually respond if your request is well thought out and asks specific questions, but a note asking “feedback, please” usually goes unanswered.
Number of Pages Required
1 page

```html
<!DOCTYPE html>
<html lang="en">
<head>
<meta charset="utf-8">
<title>Junk Removal – Stress-Free Moving &amp; Junk Removal</title>
<link href="https://fonts.googleapis.com/css2?family=Exo+2:ital,wght@1,800;1,900&family=Oswald:wght@500;600&family=PT+Sans:wght@400;700&display=swap" rel="stylesheet">
<style>
:root{
  --dark:#231f20;
  --green:#4aac3c;
  --green-btn:#3c9d31;
  --green-deep:#2f5a2b;
  --white:#ffffff;
  --ink:#231f20;
  --muted:#d8d8d8;
}
*{box-sizing:border-box;margin:0;padding:0}
html,body{width:1200px;height:3377px;overflow:hidden;background:var(--dark)}
body{position:relative;font-family:"PT Sans",sans-serif;color:var(--white)}
.abs{position:absolute}
.display{font-family:"Exo 2",sans-serif;font-style:italic;font-weight:900;letter-spacing:.5px}
.cond{font-family:"Oswald",sans-serif;font-weight:500;text-transform:uppercase}
.btn{position:absolute;display:flex;align-items:center;justify-content:center;background:var(--green-btn);color:var(--white);font-weight:700;font-size:15px;border-radius:3px;text-transform:uppercase}
.btn-dark{background:var(--dark)}
.brand{font-family:"PT Sans",sans-serif;font-weight:700;color:var(--white);line-height:.95;text-transform:uppercase}

/* header */
.site-header{left:0;top:0;width:1200px;height:100px;background:var(--dark)}
.site-header .brand{left:162px;top:18px;font-size:36px}
.phone{left:736px;top:17px;display:flex;align-items:center;gap:10px;font-size:22px;font-weight:700}
.phone-icon{width:30px;height:30px;background:var(--green-btn);border-radius:3px;display:flex;align-items:center;justify-content:center}
.main-nav{right:163px;top:65px;display:flex;gap:15px;font-size:14px;font-weight:700;text-transform:uppercase}

/* hero */
.hero-photo{left:0;top:100px;width:1200px;height:625px;background:linear-gradient(110deg,#6a7a2c 0%,#8fb53a 30%,#5a6a3a 55%,#3d4a28 80%,#2e3522 100%)}
.hero-line{left:0;top:722px;width:1200px;height:6px;background:var(--green)}
.hero-title{right:163px;top:175px;text-align:right;font-size:60px;line-height:63px;text-shadow:0 2px 6px rgba(0,0,0,.35)}
.hero-sub{right:163px;top:376px;font-size:17px;font-weight:700}
.zip{left:797px;top:421px;width:240px;height:42px;background:var(--white);border-radius:4px;color:var(--ink);font-size:14px;font-weight:700;padding:12px 10px}

/* features */
.features-frame{left:158px;top:618px;width:883px;height:270px;border:4px solid var(--white);border-bottom-width:4px;border-radius:42px 42px 0 0;overflow:hidden;display:flex}
.feature{height:100%;text-align:center;padding-top:56px}
.feature.green{background:var(--green)}
.feature.darkf{background:var(--dark)}
.feature h3{font-family:"Oswald",sans-serif;font-weight:500;font-size:22px;margin-top:12px;text-transform:uppercase}
.feature p{font-size:12.5px;line-height:16px;width:232px;margin:8px auto 0}
.dot{width:84px;height:84px;border-radius:50%;background:var(--green);border:6px solid var(--white)}

/* services */
.section-title{width:1200px;left:0;text-align:center;color:var(--green);font-size:48px}
.services-panel{left:483px;top:1051px;width:234px;height:285px;background:var(--green);border-radius:0 0 40px 40px}
.services-photo{left:513px;top:1070px;width:174px;height:230px;border-radius:50% 50% 40% 40%/40% 40% 30% 30%;background:linear-gradient(160deg,#4c6b3a,#2a3a2c 60%,#3a4d6a)}
.services-panel-brand{left:483px;top:1148px;width:234px;text-align:center;font-size:36px}
.svc{width:300px}
.svc h4{font-family:"Oswald",sans-serif;font-weight:500;font-size:19px;text-transform:uppercase}
.svc p{font-size:12.5px;line-height:16px;margin-top:6px}
.svc.left{text-align:right}
.svc-icon{width:84px;height:84px;border-radius:50%;border:4px solid var(--white);display:flex;align-items:center;justify-content:center}
.svc-icon.g{background:var(--green)}
.svc-icon.d{background:var(--dark)}

/* junk removal */
.jr-bg{left:0;top:1408px;width:1200px;height:500px;background:linear-gradient(90deg,#2c5227,#38692f 60%,#2c5227)}
.heading-lg{font-size:46px;color:var(--white)}
.copy{font-size:12.5px;line-height:20px;text-align:justify}
.truck{left:640px;top:1468px;width:400px;height:390px;background:linear-gradient(150deg,#e6e6e6 0 55%,#42b05c 55% 100%);border-radius:18px}

/* commercial / residential */
.split-left{left:0;top:1908px;width:600px;height:428px;background:linear-gradient(160deg,#2c3646,#3a3330 60%,#2a2622)}
.split-right{left:600px;top:1908px;width:600px;height:428px;background:linear-gradient(160deg,#f3f3f1,#e3e8e6 55%,#d9dcd3)}

/* clients */
.clients-bg{left:0;top:2336px;width:1200px;height:654px;background:linear-gradient(180deg,#4aac3c,#45a238)}
.card{width:276px;height:181px;background:var(--white);color:var(--ink);border-radius:14px;padding:42px 12px 0}
.card.dark{background:var(--dark);color:var(--white)}
.card h5{font-family:"Oswald",sans-serif;font-weight:500;font-size:21px;text-transform:uppercase}
.card p{font-size:12.5px;line-height:16px;margin-top:6px}
.card .who{font-size:13px;font-weight:700;margin-top:14px;text-transform:uppercase}
.quote{position:absolute;right:6px;top:-14px;font-family:"Exo 2",sans-serif;font-style:italic;font-weight:900;font-size:96px;line-height:1;color:var(--green)}

/* footer */
.footer-brand{left:162px;top:3115px;font-size:64px}
.foot-h{font-family:"Oswald",sans-serif;font-weight:500;font-size:21px;text-transform:uppercase}
.quick{left:475px;top:3068px}
.quick ul{list-style:none;margin-top:10px;font-size:12px;font-weight:700;line-height:20px;text-transform:uppercase}
.field{background:var(--white);color:var(--ink);font-size:13px;font-weight:700;padding:11px 6px;border-radius:2px}
.rule{left:162px;top:3312px;width:875px;height:1px;background:#6a6a6a}
.copyright{left:0;top:3337px;width:1200px;text-align:center;font-size:15px}
</style>
</head>
<body>

<header class="abs site-header">
  <div class="abs brand">Junk<br>Removal</div>
  <div class="abs phone">
    <span class="phone-icon"><svg width="16" height="16" viewBox="0 0 24 24"><path fill="#fff" d="M6.6 10.8a15.1 15.1 0 0 0 6.6 6.6l2.2-2.2c.3-.3.7-.4 1-.2 1.1.4 2.3.6 3.6.6.6 0 1 .4 1 1V20c0 .6-.4 1-1 1A17 17 0 0 1 3 4c0-.6.4-1 1-1h3.5c.6 0 1 .4 1 1 0 1.3.2 2.5.6 3.6.1.3 0 .7-.2 1z"/></svg></span>
    1-800-555-0199
  </div>
  <div class="btn" style="left:950px;top:18px;width:87px;height:30px;font-size:13px">Book Now</div>
  <nav class="abs main-nav"><span>Home</span><span>Who We Are</span><span>What We Remove</span><span>Jobs We Do</span><span>Our Work</span><span>Blog</span><span>FAQ</span><span>Contact Us</span></nav>
</header>

<div class="abs hero-photo" role="img" aria-label="Worker in a hard hat and safety vest loading a yellow bin into a green junk removal truck"></div>
<div class="abs hero-line"></div>
<h1 class="abs display hero-title">Stress-Free<br>Moving &amp; Junk<br>Removal</h1>
<div class="abs hero-sub">ALL YOU HAVE TO DO IS POINT!</div>
<div class="abs zip">Enter Your ZIP Code</div>
<div class="btn" style="left:891px;top:479px;width:146px;height:43px;font-size:13px">Check Availability</div>

<section class="abs features-frame">
  <div class="feature green" style="width:284px">
    <svg width="60" height="56" viewBox="0 0 60 56"><path d="M30 4a13 13 0 0 0-13 13c0 10 13 24 13 24s13-14 13-24A13 13 0 0 0 30 4z" fill="none" stroke="#fff" stroke-width="4"/><circle cx="30" cy="17" r="5" fill="#fff"/><ellipse cx="30" cy="46" rx="24" ry="6" fill="none" stroke="#fff" stroke-width="3"/></svg>
    <h3>Find a Location</h3>
    <p>Nemo enim ipsam voluptatem quia volup tas sit aspernatur aut odit aut fugit sed quia consequuntur magni dolores</p>
  </div>
  <div class="feature darkf" style="width:304px">
    <svg width="60" height="56" viewBox="0 0 60 56"><circle cx="28" cy="20" r="15" fill="none" stroke="#fff" stroke-width="3"/><text x="28" y="27" font-size="20" font-weight="700" text-anchor="middle" fill="#fff" font-family="PT Sans,sans-serif">$</text><path d="M6 44h14l10 4 22-10" fill="none" stroke="#fff" stroke-width="3"/></svg>
    <h3>Our Pricing</h3>
    <p>Nemo enim ipsam voluptatem quia volup tas sit aspernatur aut odit aut fugit sed quia consequuntur magni dolores</p>
  </div>
  <div class="feature green" style="width:287px">
    <div style="height:56px;font-family:'Exo 2',sans-serif;font-style:italic;font-weight:900;font-size:100px;line-height:80px">&ldquo;</div>
    <h3>Get a Free Quote Online</h3>
    <p>Nemo enim ipsam voluptatem quia volup tas sit aspernatur aut odit aut fugit sed quia consequuntur magni dolores</p>
  </div>
</section>
<div class="abs dot" style="left:119px;top:831px"></div>
<div class="abs dot" style="left:995px;top:831px"></div>

<h2 class="abs display section-title" style="top:958px">OUR SERVICES</h2>
<div class="abs services-panel"></div>
<div class="abs services-photo" role="img" aria-label="Junk removal crew sorting bins inside a truck"></div>
<div class="abs brand services-panel-brand">Junk<br>Removal</div>

<div class="abs svc left" style="left:140px;top:1092px"><h4>Full-Service Moving Company</h4><p>Nemo enim ipsam voluptatem quia volup<br>tas sit aspernatur aut odit aut fugit sed quia<br>consequuntur magni dolores</p></div>
<div class="abs svc left" style="left:140px;top:1205px"><h4>Hourly Moving &amp; Packing Services</h4><p>Nemo enim ipsam voluptatem quia volup<br>tas sit aspernatur aut odit aut fugit sed quia<br>consequuntur magni dolores</p></div>
<div class="abs svc" style="left:762px;top:1092px"><h4>Junk Removal &amp; Trash Pickup</h4><p>Nemo enim ipsam voluptatem quia volup<br>tas sit aspernatur aut odit aut fugit sed quia<br>consequuntur magni dolores</p></div>
<div class="abs svc" style="left:762px;top:1205px"><h4>Donation Pickups</h4><p>Nemo enim ipsam voluptatem quia volup<br>tas sit aspernatur aut odit aut fugit sed quia<br>consequuntur magni dolores</p></div>

<div class="abs svc-icon g" style="left:442px;top:1086px"><svg width="46" height="34" viewBox="0 0 46 34"><rect x="2" y="6" width="26" height="18" fill="#fff"/><path d="M28 12h9l6 7v5H28z" fill="#fff"/><circle cx="11" cy="27" r="4" fill="#fff" stroke="#4aac3c" stroke-width="2"/><circle cx="35" cy="27" r="4" fill="#fff" stroke="#4aac3c" stroke-width="2"/></svg></div>
<div class="abs svc-icon d" style="left:442px;top:1198px"><svg width="40" height="40" viewBox="0 0 40 40"><path d="M6 12l14-7 14 7v16l-14 7-14-7z" fill="none" stroke="#fff" stroke-width="3"/><path d="M6 12l14 7 14-7M20 19v16" fill="none" stroke="#fff" stroke-width="3"/></svg></div>
<div class="abs svc-icon d" style="left:674px;top:1086px"><svg width="34" height="40" viewBox="0 0 34 40"><rect x="3" y="6" width="28" height="5" fill="#fff"/><rect x="12" y="1" width="10" height="5" fill="none" stroke="#fff" stroke-width="2"/><path d="M6 12h22l-2 26H8z" fill="none" stroke="#fff" stroke-width="3"/><path d="M13 16v18M17 16v18M21 16v18" stroke="#fff" stroke-width="2"/></svg></div>
<div class="abs svc-icon g" style="left:674px;top:1198px"><svg width="40" height="40" viewBox="0 0 40 40"><path d="M4 28h32v8H4z" fill="none" stroke="#fff" stroke-width="3"/><path d="M14 24l14-16 4 4-14 16z" fill="none" stroke="#fff" stroke-width="3"/></svg></div>

<section>
  <div class="abs jr-bg" role="img" aria-label="Faded green-tinted photo of a junk removal truck"></div>
  <h2 class="abs display heading-lg" style="left:162px;top:1487px">JUNK REMOVAL</h2>
  <div class="abs copy" style="left:162px;top:1555px;width:423px">
    <p>Nemo enim ipsam voluptatem quia voluptas sit aspernatur aut odit aut fugit, sed quia consequuntur magni dolores eos qui ratione voluptatem sequi nesciunt. Neque porro quisquam est, qui dolorem ipsum quia dolor sit amet, consectetur, adipisci velit, sed quia non numquam eius modi tempora incidunt ut labore et dolore magnam aliquam quaerat voluptatem.</p>
    <p style="margin-top:13px">Nemo enim ipsam voluptatem quia voluptas sit aspernatur aut odit aut fugit, sed quia consequuntur magni dolores eos qui ratione voluptatem sequi nesciunt. Neque porro quisquam est, qui dolorem ipsum quia dolor sit amet, consectetur, adipisci velit, sed quia non numquam eius modi tempora incidunt ut labore et dolore magnam aliquam quaerat voluptatem.</p>
  </div>
  <div class="btn" style="left:162px;top:1799px;width:117px;height:38px">Read More</div>
  <div class="abs truck" role="img" aria-label="Illustration of a white box truck with a green cab"></div>
</section>

<section>
  <div class="abs split-left" role="img" aria-label="Dark photo of a commercial building under construction"></div>
  <div class="abs split-right" role="img" aria-label="Light photo of a worker hauling residential junk"></div>
  <svg class="abs" style="left:162px;top:1960px" width="72" height="70" viewBox="0 0 72 70"><rect x="4" y="14" width="40" height="54" fill="#fff"/><rect x="44" y="4" width="24" height="64" fill="#fff"/><g fill="#2c3646"><rect x="10" y="22" width="8" height="7"/><rect x="24" y="22" width="8" height="7"/><rect x="10" y="36" width="8" height="7"/><rect x="24" y="36" width="8" height="7"/><rect x="10" y="50" width="8" height="7"/><rect x="24" y="50" width="8" height="7"/><rect x="50" y="14" width="12" height="5"/><rect x="50" y="28" width="12" height="5"/><rect x="50" y="42" width="12" height="5"/></g></svg>
  <h2 class="abs display heading-lg" style="left:162px;top:2040px">COMMERCIAL</h2>
  <p class="abs copy" style="left:162px;top:2107px;width:408px">Nemo enim ipsam voluptatem quia voluptas sit aspernatur aut odit aut fugit, sed quia consequuntur magni dolores eos qui ratione voluptatem sequi nesciunt. Neque porro quisquam est, qui dolorem ipsum quia dolor sit amet, consectetur, adipisci velit, sed quia non numquam eius modi tempora incidunt ut labore et dolore magnam aliquam quaerat voluptatem.</p>
  <div class="btn" style="left:162px;top:2233px;width:117px;height:38px">Read More</div>

  <svg class="abs" style="left:630px;top:1962px" width="72" height="66" viewBox="0 0 72 66"><path d="M36 2L4 20h64z" fill="#231f20"/><rect x="8" y="22" width="56" height="42" fill="#231f20"/><g fill="#f0f0ee"><rect x="14" y="28" width="8" height="8"/><rect x="50" y="28" width="8" height="8"/><rect x="14" y="44" width="8" height="8"/><rect x="50" y="44" width="8" height="8"/><rect x="30" y="42" width="12" height="22"/><rect x="31" y="27" width="10" height="8"/></g></svg>
  <h2 class="abs display heading-lg" style="left:630px;top:2040px;color:var(--ink)">RESIDENTIAL</h2>
  <p class="abs copy" style="left:630px;top:2107px;width:407px;color:var(--ink)">Nemo enim ipsam voluptatem quia voluptas sit aspernatur aut odit aut fugit, sed quia consequuntur magni dolores eos qui ratione voluptatem sequi nesciunt. Neque porro quisquam est, qui dolorem ipsum quia dolor sit amet, consectetur, adipisci velit, sed quia non numquam eius modi tempora incidunt ut labore et dolore magnam aliquam quaerat voluptatem.</p>
  <div class="btn btn-dark" style="left:630px;top:2233px;width:117px;height:38px">Read More</div>
</section>

<section>
  <div class="abs clients-bg" role="img" aria-label="Green-tinted photo of a junk removal crew"></div>
  <h2 class="abs display section-title" style="top:2408px;color:var(--white)">OUR HAPPY CLIENTS</h2>

  <div class="abs card" style="left:162px;top:2508px"><span class="quote">&rdquo;</span><h5>Had a Great Service</h5><p>Nemo enim ipsam voluptatem quia volup tas sit aspernatur aut odit aut fugit sed quia consequuntur magni dolores</p><div class="who">- John Smith</div></div>
  <div class="abs card dark" style="left:462px;top:2508px"><span class="quote" style="color:var(--white)">&rdquo;</span><h5>Had a Great Service</h5><p>Nemo enim ipsam voluptatem quia volup tas sit aspernatur aut odit aut fugit sed quia consequuntur magni dolores</p><div class="who">- Andrews</div></div>
  <div class="abs card" style="left:761px;top:2508px"><span class="quote">&rdquo;</span><h5>Had a Great Service</h5><p>Nemo enim ipsam voluptatem quia volup tas sit aspernatur aut odit aut fugit sed quia consequuntur magni dolores</p><div class="who">- Clara James</div></div>
  <div class="abs card" style="left:162px;top:2720px"><span class="quote">&rdquo;</span><h5>Had a Great Service</h5><p>Nemo enim ipsam voluptatem quia volup tas sit aspernatur aut odit aut fugit sed quia consequuntur magni dolores</p><div class="who">- Jack Bardom</div></div>
  <div class="abs card" style="left:462px;top:2720px"><span class="quote">&rdquo;</span><h5>Had a Great Service</h5><p>Nemo enim ipsam voluptatem quia volup tas sit aspernatur aut odit aut fugit sed quia consequuntur magni dolores</p><div class="who">- Emily John</div></div>
  <div class="abs card" style="left:761px;top:2720px"><span class="quote">&rdquo;</span><h5>Had a Great Service</h5><p>Nemo enim ipsam voluptatem quia volup tas sit aspernatur aut odit aut fugit sed quia consequuntur magni dolores</p><div class="who">- John Smith</div></div>
</section>

<footer>
  <div class="abs brand footer-brand">Junk<br>Removal</div>
  <div class="abs quick">
    <div class="foot-h">Quick Links</div>
    <ul><li>Home</li><li>Who We Are</li><li>What We Remove</li><li>Jobs We Do</li><li>Our Work</li><li>Blog</li><li>FAQ</li><li>Contact Us</li></ul>
  </div>
  <div class="abs foot-h" style="left:671px;top:3068px">Get in Touch</div>
  <div class="abs field" style="left:671px;top:3100px;width:179px;height:40px">Email</div>
  <div class="abs field" style="left:859px;top:3100px;width:178px;height:40px">Number</div>
  <div class="abs field" style="left:671px;top:3151px;width:366px;height:73px">Message</div>
  <div class="btn" style="left:671px;top:3235px;width:100px;height:36px">Subscribe</div>
  <div class="abs rule"></div>
  <div class="abs copyright">Copyrights @ 2023 Junk Removal. All Rights Reserved.</div>
</footer>

</body>
</html>
```